Rack card for Self Storage Company. Distributed to all potential customers.

2 sided 4x9 multi color card
We use this rack card to give to potential customers that visit our store so that they can leave with something that has all of our most important information. We also use these as promotional items in Chamber of Commerce welcome centers. The card should be easy to read and eye catching. Not cluttered but with a decent amount of information.

Target Market(s)

Our target market is anyone with a life situation that requires storage (both long and short term). We have found that 60% of our customers come from Female age 35-60 demographic

Industry/Entity Type

Self Storage

Font styles to use
Sans Serif

Colors

Designer to choose colors to be used in the design.

Requirements
Must have
• Two sided multicolor design.
• We would like to have the company logo, address, phone number, website, email address, pictures, map, place for note taking. Include the bullet points from the existing brochure (see attached) but eliminate "Office open during access hours"
• Include the tagline "Locally owned and operated since 1989"
Nice to have
• Good use of pictures, clean, modern, eye catching design. Somewhat larger font than existing.
Should not have
• Eliminate toll free number

```html
<!DOCTYPE html>
<html lang="en">
<head>
<meta charset="utf-8">
<title>Harbor Keep Storage Center – Rack Card</title>
<link rel="stylesheet" href="https://fonts.googleapis.com/css2?family=Montserrat:wght@500;600;700;800&family=Lobster&display=swap">
<style>
  :root{
    --magenta:#a3004a;
    --wine:#7e0a3d;
    --rose:#c5306a;
    --blush:#e6a4b8;
    --paper:#ffffff;
    --note:#eeeeee;
    --line:#c9c9c9;
    --ink:#1d1d1d;
    --stage:#454b4e;
  }
  *{box-sizing:border-box;margin:0;padding:0}
  html,body{width:1200px;height:2167px;overflow:hidden}
  body{background:var(--stage);font-family:"Montserrat",sans-serif;color:var(--ink);position:relative}
  .card{position:absolute;top:476px;width:540px;height:1215px;background:var(--paper);overflow:hidden;box-shadow:0 6px 18px rgba(0,0,0,.35)}
  .card--front{left:40px}
  .card--back{left:620px}
  .abs{position:absolute}

  /* brand */
  .brand{left:0;right:0;top:40px;text-align:center}
  .brand__name{font-family:"Montserrat",sans-serif;font-weight:800;font-size:50px;color:var(--magenta);letter-spacing:1px;line-height:1}
  .brand__rule{height:2px;background:var(--blush);margin:8px auto 0;width:380px}
  .brand__sub{font-weight:800;font-size:17px;letter-spacing:3px;color:var(--magenta);margin-top:8px}

  /* front band */
  .hero-band{left:0;right:0;top:194px;height:214px;background:linear-gradient(180deg,var(--wine),var(--magenta))}
  .hero-rule{left:0;right:0;top:207px;height:2px;background:#fff}
  .sq{position:absolute;background:var(--rose)}
  .tagline{left:0;right:0;top:274px;text-align:center;font-family:"Lobster",cursive;color:#fff;font-size:28px;line-height:34px}
  .photo{background:linear-gradient(180deg,#b7c7d6 0%,#d9b79a 40%,#c39d7b 70%,#7d8a5e 100%)}
  .photo--building{left:0;right:0;top:406px;height:272px}
  .photo--units{top:989px;height:117px;width:236px;background:linear-gradient(180deg,#8fb2d8 0%,#d7d3cc 45%,#8a5a3c 70%,#b9b6ae 100%)}
  .photo--hall{top:989px;height:117px;width:236px;background:linear-gradient(90deg,#6e4a30,#c6a17c 40%,#e5e0d8 50%,#c6a17c 60%,#6e4a30)}

  .feature{width:147px;height:99px;border:1px solid #9a9a9a;text-align:center;font-weight:600;font-size:14px;line-height:17px;padding-top:38px}
  .feature__icon{position:absolute;left:50%;top:-22px;margin-left:-24px;width:48px;height:48px;border-radius:50%;background:#fff}

  .footer-band{left:0;right:0;top:1127px;height:61px;background:var(--magenta);color:#fff;text-align:center;font-weight:600;font-size:30px;line-height:61px;letter-spacing:.5px}
  .website{left:0;right:0;top:1196px;text-align:center;font-weight:600;font-size:14px;letter-spacing:4.5px}

  /* back */
  .back-band{left:0;right:0;top:173px;bottom:0;background:linear-gradient(180deg,var(--wine),var(--magenta) 35%)}
  .map-frame{left:91px;top:45px;width:363px;height:365px;background:#fff;border:3px solid var(--magenta);padding:5px}
  .map{width:100%;height:100%;border:2px solid var(--magenta);background:linear-gradient(135deg,#fbfbfb,#f1eef0)}
  .location{left:0;right:0;top:440px;text-align:center;color:#fff}
  .location__city{font-weight:800;font-size:38px;letter-spacing:1px}
  .location__addr{font-weight:500;font-size:18px;line-height:23px;margin-top:4px}
  .phone{left:0;right:0;top:555px;display:flex;justify-content:center;align-items:center;gap:12px;color:#fff;font-weight:800;font-size:46px}
  .email{left:0;right:0;top:630px;text-align:center;color:#fff;font-size:17px;font-weight:500}
  .hours{left:75px;top:685px;display:flex;align-items:center;color:#fff;gap:14px}
  .hours__day{font-weight:700;font-size:20px}
  .hours__time{font-size:17px;font-weight:500}
  .hours__divider{width:2px;height:48px;background:#fff;margin:0 6px}
  .notes{left:66px;top:763px;width:410px;height:452px;background:linear-gradient(180deg,#f7f7f7,var(--note));border-top-right-radius:16px}
  .notes__tab{position:absolute;right:0;top:8px;background:var(--magenta);color:#fff;font-family:"Lobster",cursive;font-size:17px;padding:2px 14px 3px 10px}
  .notes__lines{position:absolute;left:46px;right:30px;top:54px;bottom:10px;background:repeating-linear-gradient(180deg,transparent 0 26px,var(--line) 26px 27px)}
  .ring{position:absolute;left:-6px;width:26px;height:12px}
</style>
</head>
<body>

<!-- FRONT -->
<section class="card card--front" aria-label="Rack card front">
  <header class="abs brand">
    <div class="brand__name">HARBOR KEEP</div>
    <div class="brand__rule"></div>
    <div class="brand__sub">STORAGE CENTER</div>
  </header>

  <div class="abs hero-band">
    <span class="sq" style="left:270px;top:0;width:70px;height:40px"></span>
    <span class="sq" style="left:345px;top:50px;width:28px;height:28px"></span>
    <span class="sq" style="left:68px;top:130px;width:28px;height:28px"></span>
    <span class="sq" style="left:0;top:170px;width:62px;height:44px"></span>
    <span class="sq" style="left:475px;top:172px;width:28px;height:28px"></span>
    <span class="sq" style="left:110px;top:196px;width:70px;height:18px"></span>
  </div>
  <div class="abs hero-rule"></div>
  <p class="abs tagline">Locally owned and operated since 1989<br>For all your storage needs!</p>

  <div class="abs photo photo--building" role="img" aria-label="Photo of the storage center office building with palm trees"></div>

  <div class="abs feature" style="left:27px;top:726px">
    <svg class="feature__icon" viewBox="0 0 48 48"><circle cx="24" cy="24" r="21" fill="none" stroke="#a3004a" stroke-width="3"/><circle cx="24" cy="24" r="16" fill="#a3004a"/><path d="M24 13l8 3v6c0 6-4 10-8 12-4-2-8-6-8-12v-6z" fill="#fff"/><path d="M20 23l3 3 5-6" stroke="#a3004a" stroke-width="2" fill="none"/></svg>
    Clean<br>and<br>secure
  </div>
  <div class="abs feature" style="left:196px;top:726px">
    <svg class="feature__icon" viewBox="0 0 48 48"><circle cx="24" cy="24" r="21" fill="none" stroke="#a3004a" stroke-width="3"/><circle cx="24" cy="24" r="16" fill="#a3004a"/><circle cx="28" cy="20" r="4" fill="#fff"/><rect x="15" y="22" width="10" height="6" rx="3" fill="#fff"/><path d="M20 29v6" stroke="#fff" stroke-width="2"/></svg>
    Climate<br>controlled<br>units
  </div>
  <div class="abs feature" style="left:364px;top:726px">
    <svg class="feature__icon" viewBox="0 0 48 48"><circle cx="24" cy="24" r="21" fill="none" stroke="#a3004a" stroke-width="3"/><circle cx="24" cy="24" r="16" fill="#a3004a"/><path d="M16 16l16 16M32 16L16 32" stroke="#fff" stroke-width="2.5"/><rect x="21" y="21" width="6" height="6" fill="#fff"/></svg>
    Large<br>selection<br>of sizes
  </div>
  <div class="abs feature" style="left:112px;top:868px">
    <svg class="feature__icon" viewBox="0 0 48 48"><circle cx="24" cy="24" r="21" fill="none" stroke="#a3004a" stroke-width="3"/><circle cx="24" cy="24" r="16" fill="#a3004a"/><rect x="15" y="17" width="18" height="15" rx="1" fill="#fff"/><rect x="15" y="17" width="18" height="4" fill="#e6a4b8"/></svg>
    Open<br>7 days<br>a week
  </div>
  <div class="abs feature" style="left:280px;top:868px">
    <svg class="feature__icon" viewBox="0 0 48 48"><circle cx="24" cy="24" r="21" fill="none" stroke="#a3004a" stroke-width="3"/><circle cx="24" cy="24" r="16" fill="#a3004a"/><path d="M16 32l14-14M24 18h6v6M20 32l10-10" stroke="#fff" stroke-width="2.5" fill="none"/></svg>
    Complite<br>selection of<br>moving supplies
  </div>

  <div class="abs photo--units" style="left:25px" role="img" aria-label="Photo of a row of outdoor storage unit doors"></div>
  <div class="abs photo--hall" style="left:273px" role="img" aria-label="Photo of an indoor storage hallway"></div>

  <div class="abs footer-band">Alder Point - 555.014.2380</div>
  <div class="abs website">www.harborkeepstorage.com</div>
</section>

<!-- BACK -->
<section class="card card--back" aria-label="Rack card back">
  <div class="abs back-band">
    <span class="sq" style="left:514px;top:0;width:26px;height:28px"></span>
    <span class="sq" style="left:480px;top:40px;width:60px;height:68px"></span>
    <span class="sq" style="left:60px;top:70px;width:30px;height:28px"></span>
    <span class="sq" style="left:72px;top:240px;width:70px;height:70px"></span>
    <span class="sq" style="left:150px;top:240px;width:28px;height:22px"></span>
  </div>

  <div class="abs map-frame">
    <div class="map" role="img" aria-label="Street map showing the location near the turnpike and interstate exits"></div>
  </div>

  <div class="abs location">
    <div class="location__city">ALDER POINT</div>
    <div class="location__addr">4820 SW Cedar Ridge Blvd<br>Alder Point, FL 30000</div>
  </div>

  <div class="abs phone">
    <svg width="42" height="42" viewBox="0 0 42 42"><circle cx="21" cy="21" r="20" fill="#fff"/><path d="M15 11c-2 1-3 3-2 6 2 6 7 11 13 13 3 1 5 0 6-2l-4-4-3 2c-3-1-6-4-7-7l2-3z" fill="#a3004a"/></svg>
    <span>555.014.2380</span>
  </div>
  <div class="abs email">Email: info@harborkeepstorage.com</div>

  <div class="abs hours">
    <svg width="42" height="42" viewBox="0 0 42 42"><circle cx="21" cy="21" r="19" fill="#fff"/><path d="M21 10v11l7 5" stroke="#a3004a" stroke-width="2.5" fill="none"/></svg>
    <div><div class="hours__day">Mon.-sat.</div><div class="hours__time">7a.m to 6.30p.m</div></div>
    <span class="hours__divider"></span>
    <div><div class="hours__day">Sun.</div><div class="hours__time">9a.m to 4.30p.m</div></div>
  </div>

  <div class="abs notes">
    <div class="notes__tab">Notes</div>
    <div class="notes__lines"></div>
    <svg class="ring" style="top:28px" viewBox="0 0 26 12"><path d="M0 6h14" stroke="#a3004a" stroke-width="3"/><circle cx="18" cy="6" r="5" fill="#a3004a"/></svg>
    <svg class="ring" style="top:78px" viewBox="0 0 26 12"><path d="M0 6h14" stroke="#a3004a" stroke-width="3"/><circle cx="18" cy="6" r="5" fill="#a3004a"/></svg>
    <svg class="ring" style="top:128px" viewBox="0 0 26 12"><path d="M0 6h14" stroke="#a3004a" stroke-width="3"/><circle cx="18" cy="6" r="5" fill="#a3004a"/></svg>
    <svg class="ring" style="top:178px" viewBox="0 0 26 12"><path d="M0 6h14" stroke="#a3004a" stroke-width="3"/><circle cx="18" cy="6" r="5" fill="#a3004a"/></svg>
    <svg class="ring" style="top:228px" viewBox="0 0 26 12"><path d="M0 6h14" stroke="#a3004a" stroke-width="3"/><circle cx="18" cy="6" r="5" fill="#a3004a"/></svg>
    <svg class="ring" style="top:278px" viewBox="0 0 26 12"><path d="M0 6h14" stroke="#a3004a" stroke-width="3"/><circle cx="18" cy="6" r="5" fill="#a3004a"/></svg>
    <svg class="ring" style="top:328px" viewBox="0 0 26 12"><path d="M0 6h14" stroke="#a3004a" stroke-width="3"/><circle cx="18" cy="6" r="5" fill="#a3004a"/></svg>
    <svg class="ring" style="top:378px" viewBox="0 0 26 12"><path d="M0 6h14" stroke="#a3004a" stroke-width="3"/><circle cx="18" cy="6" r="5" fill="#a3004a"/></svg>
    <svg class="ring" style="top:428px" viewBox="0 0 26 12"><path d="M0 6h14" stroke="#a3004a" stroke-width="3"/><circle cx="18" cy="6" r="5" fill="#a3004a"/></svg>
  </div>
</section>

</body>
</html>
```